Customer Journey Graphic

I want to graphic to describe a marketing framework I am teaching a course on

It a framework for growing a business
The idea is we
get customers to "take a Journey" through 7 steps
to deliver value to them

There are 4 major concepts that impact this journey - Game Plan, Business Model, "Inside out thinking' and Unique Competitive advantage
These concepts can make the journey faster, get more people to take it or make it more valuable

The stages are

- Target
- attract
- nurture
- convert
- maximise
- loyalty
- reactivation

I want to uses this framework as an overall;; 'explainer' fro my idea ,so it must looks very professional, and work well in presentations

I have included a rought 'sketch; of my thinking as an attachment
Updates

Target Market(s)

Business Owners

Industry/Entity Type

Business

Font styles to use
Serif

Requirements
Must have
• clear, get acroess the idea of a Journye over times, teh idea you can improve your results throught applying concpets of ' business model', "inside out thinking: , unique competitive advantage and game plane

```html
<!DOCTYPE html>
<html lang="en">
<head>
<meta charset="utf-8">
<title>Customer Journey Framework</title>
<link href="https://fonts.googleapis.com/css2?family=Anton&family=Oswald:wght@600&display=swap" rel="stylesheet">
<style>
  :root {
    --green: #45b649;
    --cyan: #5bc4d1;
    --orange: #f58220;
    --red: #f26b65;
    --tile: #000000;
    --ink-light: #ffffff;
    --paper: #ffffff;
  }
  html, body {
    margin: 0;
    padding: 0;
    width: 1200px;
    height: 900px;
    overflow: hidden;
    background: var(--paper);
  }
  .canvas { display: block; width: 1200px; height: 900px; }
  .segment--green { fill: var(--green); }
  .segment--cyan { fill: var(--cyan); }
  .segment--orange { fill: var(--orange); }
  .segment--red { fill: var(--red); }
  .concept-label {
    font-family: "Anton", "Impact", sans-serif;
    fill: var(--ink-light);
    letter-spacing: 1px;
  }
  .concept-label--large { font-size: 30px; }
  .concept-label--medium { font-size: 26px; }
  .concept-label--wide { font-size: 28px; letter-spacing: 4px; }
  .concept-label--spaced { font-size: 32px; letter-spacing: 4px; }
  .stage-tile { fill: var(--tile); }
  .stage-icon { fill: none; stroke: var(--ink-light); stroke-linecap: round; stroke-linejoin: round; }
  .stage-icon-fill { fill: var(--ink-light); }
  .stage-label {
    font-family: "Oswald", "Arial Narrow", sans-serif;
    font-weight: 600;
    font-size: 20px;
    text-anchor: middle;
  }
  .stage-label--green { fill: var(--green); }
  .stage-label--red { fill: var(--red); }
  .stage-label--orange { fill: var(--orange); }
  .stage-label--cyan { fill: var(--cyan); }
</style>
</head>
<body>
<svg class="canvas" viewBox="0 0 1024 768" xmlns="http://www.w3.org/2000/svg" role="img" aria-label="Customer journey framework: seven stages surrounded by four growth concepts">
  <defs>
    <path id="segment-shape" d="M502,100 A283,283 0 0 1 784.8,373.1 L726.3,406.6 L669.9,377.1 A168,168 0 0 0 502,215 L533.4,159.7 Z"/>
    <path id="track-clockwise" d="M502,595 A212,212 0 1 1 502,171 A212,212 0 1 1 502,595"/>
    <path id="track-counter-inner" d="M502,155 A228,228 0 1 0 502,611 A228,228 0 1 0 502,155"/>
    <path id="track-counter-outer" d="M502,121 A262,262 0 1 0 502,645 A262,262 0 1 0 502,121"/>
    <path id="track-counter-mid" d="M502,140 A243,243 0 1 0 502,626 A243,243 0 1 0 502,140"/>
  </defs>

  <g class="concept-ring">
    <use href="#segment-shape" class="segment--green" transform="rotate(-85 502 383)"/>
    <use href="#segment-shape" class="segment--cyan" transform="rotate(5 502 383)"/>
    <use href="#segment-shape" class="segment--orange" transform="rotate(95 502 383)"/>
    <use href="#segment-shape" class="segment--red" transform="rotate(185 502 383)"/>

    <text class="concept-label concept-label--large"><textPath href="#track-clockwise" startOffset="38.9%" text-anchor="middle">Business Model</textPath></text>
    <text class="concept-label concept-label--large"><textPath href="#track-clockwise" startOffset="63.9%" text-anchor="middle">Inside Out Thinking</textPath></text>
    <text class="concept-label concept-label--medium"><textPath href="#track-counter-inner" startOffset="61.1%" text-anchor="middle">Unique comeptitive</textPath></text>
    <text class="concept-label concept-label--wide"><textPath href="#track-counter-outer" startOffset="61.1%" text-anchor="middle">Advantage</textPath></text>
    <text class="concept-label concept-label--spaced"><textPath href="#track-counter-mid" startOffset="36.1%" text-anchor="middle">Gameplan</textPath></text>
  </g>

  <g class="stage" transform="translate(15 338)">
    <rect class="stage-tile" width="90" height="90" rx="8"/>
    <circle class="stage-icon" cx="45" cy="50" r="28" stroke-width="5"/>
    <circle class="stage-icon" cx="45" cy="50" r="16" stroke-width="5"/>
    <circle class="stage-icon-fill" cx="45" cy="50" r="6"/>
    <text class="stage-label stage-label--green" x="45" y="114">Target</text>
  </g>

  <g class="stage" transform="translate(118 338)">
    <rect class="stage-tile" width="90" height="90" rx="8"/>
    <g transform="rotate(-40 45 45)">
      <path class="stage-icon" d="M27,24 V48 A18,18 0 0 0 63,48 V24" stroke-width="11" stroke-linecap="butt"/>
      <rect class="stage-icon-fill" x="21.5" y="18" width="11" height="9"/>
      <rect class="stage-icon-fill" x="57.5" y="18" width="11" height="9"/>
    </g>
    <text class="stage-label stage-label--red" x="45" y="114">Attract</text>
  </g>

  <g class="stage" transform="translate(348 338)">
    <rect class="stage-tile" width="90" height="90" rx="8"/>
    <path class="stage-icon" d="M45,58 V30" stroke-width="4"/>
    <ellipse class="stage-icon-fill" cx="35" cy="34" rx="10" ry="5" transform="rotate(35 35 34)"/>
    <ellipse class="stage-icon-fill" cx="55" cy="30" rx="10" ry="5" transform="rotate(-35 55 30)"/>
    <ellipse class="stage-icon-fill" cx="45" cy="20" rx="5" ry="9"/>
    <path class="stage-icon" d="M14,62 Q30,56 46,66 L72,56" stroke-width="5"/>
    <path class="stage-icon" d="M14,72 L40,76 L74,64" stroke-width="5"/>
    <text class="stage-label stage-label--orange" x="45" y="114">Nurture</text>
  </g>

  <g class="stage" transform="translate(455 338)">
    <rect class="stage-tile" width="90" height="90" rx="8"/>
    <circle class="stage-icon" cx="45" cy="45" r="27" stroke-width="10" stroke-dasharray="10.6 10.6" stroke-linecap="butt"/>
    <circle class="stage-icon-fill" cx="45" cy="45" r="23"/>
    <circle class="stage-tile" cx="45" cy="45" r="10"/>
    <text class="stage-label stage-label--cyan" x="45" y="114">Convert</text>
  </g>

  <g class="stage" transform="translate(562 338)">
    <rect class="stage-tile" width="90" height="90" rx="8"/>
    <rect class="stage-icon-fill" x="20" y="62" width="10" height="14"/>
    <rect class="stage-icon-fill" x="35" y="52" width="10" height="24"/>
    <rect class="stage-icon-fill" x="50" y="42" width="10" height="34"/>
    <rect class="stage-icon-fill" x="65" y="32" width="10" height="44"/>
    <path class="stage-icon" d="M16,52 L64,16" stroke-width="4"/>
    <path class="stage-icon-fill" d="M70,12 L56,14 L66,26 Z"/>
    <text class="stage-label stage-label--green" x="45" y="114">Maximise</text>
  </g>

  <g class="stage" transform="translate(797 338)">
    <rect class="stage-tile" width="90" height="90" rx="8"/>
    <circle class="stage-icon" cx="45" cy="45" r="16" stroke-width="7" stroke-dasharray="6.3 6.3" stroke-linecap="butt"/>
    <circle class="stage-icon-fill" cx="45" cy="45" r="13"/>
    <circle class="stage-tile" cx="45" cy="45" r="5"/>
    <path class="stage-icon" d="M20,40 A26,26 0 0 1 58,22" stroke-width="4"/>
    <path class="stage-icon-fill" d="M64,24 L52,16 L54,30 Z"/>
    <path class="stage-icon" d="M70,50 A26,26 0 0 1 32,68" stroke-width="4"/>
    <path class="stage-icon-fill" d="M26,66 L38,74 L36,60 Z"/>
    <text class="stage-label stage-label--cyan" x="45" y="114">Loyalty</text>
  </g>

  <g class="stage" transform="translate(910 338)">
    <rect class="stage-tile" width="90" height="90" rx="8"/>
    <path class="stage-icon" d="M30,24 A26,26 0 1 1 20,50" stroke-width="8" stroke-linecap="butt"/>
    <path class="stage-icon-fill" d="M16,20 L38,14 L34,36 Z"/>
    <text class="stage-label stage-label--orange" x="45" y="114">Reactivation</text>
  </g>
</svg>
</body>
</html>
```